Business Card Design Project - KLB

I am looking for a more sophisticated card design for my company,
"The Lumen Collective"

We are a consultancy focused on strategy and change in Associations and professional organisations.

I am a lawyer and psychologist with a PhD and so am looking for something that communicates seriousness and credibility but also quirky creative solutions for strategic problems, which is my field of speciality.

I am looking for something that is quietly spoken, rather than loud colours ('credible' and 'creative' are the two adjectives that I think of as competing here).

I particularly like an embossed card style - heavy white card with plain white or white and black or white and grey text.

The key logo image for the company is a question mark and I am open to suggestions and ideas on design.

I have attached a file that includes a couple of styles that have caught my eye and my thoughts on them. Hopefully they communicate what I'm looking for.
Updates

Thank you for all the great suggestions and designs.

I really appreciated the effort and creative energy you put into your designs. I have now closed the project after selecting a design and advising the successful designer of the card that I am happy with.

Regards

Target Market(s)

Organisations (CEO's and Boards), Governments, Legal professionals, Membership Associations and aspiring professionals.

Industry/Entity Type

Lawyer

Requirements
Must have
• The key logo element is a question mark (?) and this needs to be incorporated.

Embossed style - cut outs or other design ideas interest me too.

The attached file has a number of sample ideas and comments on each one that I like.
Should not have
• I like crisp, modern fonts (Myriads etc...) and do not like embellished fonts or Times etc...

Files

```html
<!DOCTYPE html>
<html lang="en">
<head>
<meta charset="utf-8">
<title>The Lumen Collective – Business Card</title>
<link rel="stylesheet" href="https://fonts.googleapis.com/css2?family=Bebas+Neue&family=Montserrat:wght@700;800&family=Questrial&display=swap">
<style>
  :root {
    --stage: #0b0b0b;
    --paper: #ffffff;
    --navy: #14213d;
    --crimson: #a81c2c;
    --panel-grey: #a9a9a9;
    --rule-grey: #9a9a9a;
    --ink-white: #ffffff;
  }
  * { box-sizing: border-box; margin: 0; padding: 0; }
  html, body {
    width: 1200px; height: 900px; overflow: hidden;
    background: var(--stage);
  }
  .board { position: relative; width: 1200px; height: 900px; }

  .board-title {
    position: absolute; top: 22px; left: 0; width: 1200px;
    text-align: center; color: var(--ink-white);
    font-family: "Bebas Neue", sans-serif; font-size: 50px; letter-spacing: 0.5px;
  }

  /* front of card */
  .card-front {
    position: absolute; left: 42px; top: 106px; width: 803px; height: 415px;
    background: var(--paper); overflow: hidden;
  }
  .header-plate {
    position: absolute; left: 13px; top: 14px; width: 777px; height: 93px;
    background: var(--navy); border: 2px solid var(--navy);
    outline: 1px solid #fff; outline-offset: -5px;
  }
  .corner-ornament {
    position: absolute; top: 6px; width: 66px; height: 66px;
    background: #e6e8ee;
    clip-path: polygon(0 0, 100% 0, 100% 14%, 14% 14%, 14% 100%, 0 100%);
  }
  .corner-ornament.left { left: 6px; }
  .corner-ornament.right { right: 6px; transform: scaleX(-1); }
  .company-name {
    position: absolute; left: 0; right: 0; top: 22px; text-align: center;
    font-family: "Montserrat", sans-serif; font-weight: 800; font-size: 34px;
    color: var(--ink-white); letter-spacing: -0.5px;
  }
  .rule { position: absolute; }
  .rule-upper { left: 80px; top: 88px; }
  .rule-lower { left: 172px; top: 117px; }

  .side-block {
    position: absolute; top: 116px; width: 150px; height: 88px;
    background: linear-gradient(135deg, #4a5670, #8d95a8);
  }
  .side-block.left { left: 20px; clip-path: polygon(0 0, 100% 0, 0 100%); }
  .side-block.right { right: 18px; clip-path: polygon(0 0, 100% 0, 100% 100%); }

  .band { position: absolute; left: 0; width: 100%; background: var(--navy); }
  .band-wide { top: 261px; height: 57px; }
  .band-narrow { top: 326px; height: 35px; }

  .name-plate {
    position: absolute; left: 111px; top: 140px; width: 580px; height: 57px;
    background: var(--panel-grey); border: 2px solid #fff; text-align: center;
  }
  .person-name {
    margin-top: 5px;
    font-family: "Montserrat", sans-serif; font-weight: 700; font-size: 25px;
    color: var(--crimson);
  }
  .person-role {
    font-family: "Questrial", sans-serif; font-size: 16px; color: #fff;
    line-height: 1; margin-top: -2px;
  }
  .contact-plate {
    position: absolute; left: 111px; top: 201px; width: 580px; height: 200px;
    background: var(--panel-grey); border: 2px solid #fff;
    padding: 6px 0 0 18px; color: #fff;
  }
  .contact-label {
    font-family: "Montserrat", sans-serif; font-weight: 700; font-size: 12px;
    line-height: 1.1;
  }
  .contact-value {
    font-family: "Questrial", sans-serif; font-size: 19px; line-height: 1.1;
    margin-bottom: 2px;
  }

  /* back of card */
  .card-back {
    position: absolute; left: 489px; top: 539px; width: 647px; height: 331px;
    background: var(--paper); overflow: hidden;
  }
  .back-band {
    position: absolute; left: 0; top: 209px; width: 100%; height: 82px;
    background: var(--navy);
  }
  .brand-lockup {
    position: absolute; left: 24px; top: 120px;
    display: flex; align-items: center; gap: 14px;
  }
  .brand-name {
    font-family: "Montserrat", sans-serif; font-weight: 800; font-size: 40px;
    color: var(--panel-grey); letter-spacing: -1px;
  }
  .brand-dot {
    width: 46px; height: 46px; border-radius: 50%; background: var(--crimson);
  }

  .flip-arrow { position: absolute; left: 855px; top: 355px; }
</style>
</head>
<body>
<main class="board">
  <h1 class="board-title">The Lumen Collective – Business Card</h1>

  <section class="card-front" aria-label="Front of business card">
    <div class="header-plate">
      <div class="corner-ornament left" role="img" aria-label="Art deco corner ornament"></div>
      <div class="corner-ornament right" role="img" aria-label="Art deco corner ornament"></div>
      <p class="company-name">THE LUMEN COLLECTIVE</p>
    </div>
    <svg class="rule rule-upper" width="644" height="10" viewBox="0 0 644 10">
      <line x1="4" y1="5" x2="640" y2="5" stroke="#9a9a9a" stroke-width="1.5"/>
      <rect x="1" y="2" width="6" height="6" fill="#9a9a9a" transform="rotate(45 4 5)"/>
      <rect x="637" y="2" width="6" height="6" fill="#9a9a9a" transform="rotate(45 640 5)"/>
    </svg>
    <svg class="rule rule-lower" width="458" height="10" viewBox="0 0 458 10">
      <line x1="4" y1="5" x2="454" y2="5" stroke="#9a9a9a" stroke-width="1.5"/>
      <rect x="1" y="2" width="6" height="6" fill="#9a9a9a" transform="rotate(45 4 5)"/>
      <rect x="451" y="2" width="6" height="6" fill="#9a9a9a" transform="rotate(45 454 5)"/>
    </svg>

    <div class="side-block left" role="img" aria-label="Hatched deco line pattern"></div>
    <div class="side-block right" role="img" aria-label="Hatched deco line pattern"></div>

    <div class="band band-wide"></div>
    <div class="band band-narrow"></div>

    <div class="name-plate">
      <p class="person-name">DR MAREN HOLT</p>
      <p class="person-role">DIRECTOR</p>
    </div>
    <div class="contact-plate">
      <p class="contact-label">POST</p>
      <p class="contact-value">P.O. Box 4410, Elmhurst Park<br>Sydney, Australia</p>
      <p class="contact-label">MOBILE</p>
      <p class="contact-value">0400 123 456</p>
      <p class="contact-label">WORK</p>
      <p class="contact-value">(02) 9000 4417</p>
      <p class="contact-label">E-MAIL</p>
      <p class="contact-value">maren@lumencollective.com.au</p>
    </div>
  </section>

  <svg class="flip-arrow" width="200" height="180" viewBox="0 0 200 180" aria-hidden="true">
    <path d="M40 40 Q120 40 150 130" fill="none" stroke="#fff" stroke-width="22"/>
    <polygon points="8,40 52,6 52,74" fill="#fff"/>
    <polygon points="118,128 186,128 150,175" fill="#fff"/>
  </svg>

  <section class="card-back" aria-label="Back of business card">
    <div class="back-band"></div>
    <div class="brand-lockup">
      <span class="brand-name">The Lumen Collective</span>
      <span class="brand-dot"></span>
    </div>
  </section>
</main>
</body>
</html>
```